Website Design for Webflow platform

The existing website is tired and not enticing the reader by content or visuals or CTAs . The industry is serious and competitive and demands the business to relate to this audience. Use of graphics and video and sharp relatable imagery mixed in with content. Create an exciting professional progressive homepage design that keeps the visitor wanting to view the whole page. Create supplementary coordinated pages/templates for other pages for this new website. It should be memorable, not boring, but professional and command confidence in the business and services offered in this type of industry. This needs to be coded for Webflow platform
Updates

Target Market(s)

Emergency management professionals/decision makers from high risk industries - oil & gas, transporation airline/rail/water, government, community responders, police, fire, military, chemical, nuclear, utilities

Industry/Entity Type

Emergency management services for Industry, Big Business, Government, Education Facilities, Hospitals, Correctional Facilities, Banking, Insurance

Coding

Coded - Design and coding required

Number of Pages Required

5+ page

Font styles to use
Serif
Sans Serif
Other font styles liked:
• Ubuntu and Calibri - see Brand document attached

Colors
0094D4
00A9DD
6FCCEA
C7EBF8
E9F6FB
00AB8E
00BBA5
67D7C9
C6EFE9
E9F9F6
F0912C
F2A743
F7CA91
FBE8D2
FDF5EE
6B429C
8869AF
B7A5CE
E3DAEB
F3F0F8

Requirements
Must have
• A home page that links to other pages. Must be exciting design relative to the industry and utilize powerful images that portray the seriousness of the business
Nice to have
• Great calls to action related to the industry. Animations that are professional, not too busy but leading edge in the design and the content.
Should not have
• boring typical page layouts

```html
<!DOCTYPE html>
<html lang="en">
<head>
<meta charset="utf-8">
<title>Ridgeline Consulting — Emergency Management</title>
<link rel="stylesheet" href="https://fonts.googleapis.com/css2?family=Ubuntu:wght@500;700&family=Poppins:wght@400;500;600&display=swap">
<style>
:root{
  --navy:#1e3457;
  --navy-deep:#17284a;
  --ink:#1b1b2b;
  --heading-blue:#1f3a68;
  --orange:#f0912c;
  --orange-btn:#ea7424;
  --purple:#6b429c;
  --purple-soft:#b7a5ce;
  --blue-soft:#b9cfe0;
  --text:#4a4a5a;
  --white:#ffffff;
}
*{margin:0;padding:0;box-sizing:border-box}
html,body{width:1200px;height:5291px;overflow:hidden}
body{position:relative;font-family:"Poppins",sans-serif;color:var(--text);background:var(--white)}
.abs{position:absolute}
h1,h2,h3{font-family:"Ubuntu",sans-serif;font-weight:700}

/* hero */
.hero{left:0;top:0;width:1200px;height:790px;overflow:hidden}
.hero-photo{left:0;top:0;width:1200px;height:790px;background:linear-gradient(180deg,#2a2440 0%,#3c3550 30%,#43404a 55%,#2d2a34 80%,#1a1a26 100%)}
.hero-shade{left:0;top:0;width:1200px;height:790px;background:linear-gradient(90deg,rgba(20,18,35,.55),rgba(20,18,35,.1))}
.brand{display:flex;align-items:center;gap:10px;color:var(--white);font-family:"Poppins",sans-serif;font-weight:600;font-size:24px}
.brand-mark{width:34px;height:34px;border:3px solid var(--white)}
.nav{display:flex;gap:26px;font-size:13px;color:var(--white)}
.call{display:flex;align-items:center;gap:10px;color:var(--white)}
.call-icon{width:36px;height:36px;border-radius:50%;background:var(--purple);display:flex;align-items:center;justify-content:center}
.call small{display:block;font-size:10px;opacity:.85}
.call strong{font-size:15px;font-weight:600}
.btn{background:var(--orange-btn);color:var(--white);font-size:12px;font-weight:500;display:flex;align-items:center;justify-content:center}
.location{font-size:12px;color:var(--white);display:flex;gap:6px;align-items:center}
.hero-title{left:140px;top:280px;font-size:66px;color:var(--orange);letter-spacing:1px}
.hero-title2{left:140px;top:366px;font-size:52px;color:var(--white);font-weight:500}
.hero-sub{left:140px;top:458px;font-family:"Ubuntu",sans-serif;font-weight:500;font-size:20px;color:var(--white)}
.play{left:804px;top:305px;width:82px;height:82px;border-radius:50%;background:var(--white);border:5px solid rgba(255,255,255,.5);background-clip:padding-box;display:flex;align-items:center;justify-content:center}
.dots{left:560px;top:638px;display:flex;gap:8px}
.dots span{width:8px;height:8px;border-radius:50%;background:var(--white)}

/* intro */
.intro-bg{left:0;top:780px;width:1200px;height:1500px;background:linear-gradient(180deg,#eef0f6 0%,#fafbfd 35%,#ffffff 100%)}
.intro{left:392px;top:830px;width:662px;font-size:12.5px;line-height:24px;text-align:justify;color:#333}

.leader-photo{left:144px;top:1036px;width:382px;height:470px;background:linear-gradient(160deg,#3b6aa8 0%,#8fb0d6 40%,#2c3a55 100%)}
.why-title{left:625px;top:1088px;font-size:34px;line-height:48px;color:var(--ink)}
.why-title span{color:var(--heading-blue)}
.why-text{left:625px;top:1202px;width:430px;font-size:12.5px;line-height:24px;text-align:justify}
.why-text p{margin-bottom:14px}
.checks{left:625px;top:1384px;font-size:12.5px;font-weight:500;color:#222;list-style:none}
.checks li{display:flex;align-items:center;gap:12px;height:33px}
.quote{left:273px;top:1556px;width:620px;font-size:12.5px;line-height:24px;color:#444}
.quote strong{display:block;color:var(--heading-blue);font-weight:500;font-size:14px}

.stats{left:144px;top:1718px;width:912px;height:181px;background:var(--navy);border-radius:4px;display:flex;align-items:center;color:var(--white)}
.stat{display:flex;align-items:center;gap:12px;font-size:14px;opacity:.95}
.stat b{font-size:40px;font-weight:400}
.stat-sep{width:1px;height:74px;background:rgba(255,255,255,.25)}

.trusted{left:0;width:1200px;top:1978px;text-align:center;font-family:"Ubuntu",sans-serif;font-weight:500;font-size:19px;color:var(--ink)}
.logos{left:64px;top:2045px;display:flex;gap:12px}
.logo-tile{width:203px;height:103px;background:#eeeeef;display:flex;align-items:center;justify-content:center;text-align:center;font-size:15px;font-weight:600;color:#6a6f7a;padding:0 10px}
.view-btn{left:484px;top:2180px;width:232px;height:37px}

/* solutions */
.solutions{left:0;top:2326px;width:1200px;height:606px;background:linear-gradient(135deg,#eceef8,#f8f8fc 50%,#e9ebf5)}
.sec-title{left:0;width:1200px;text-align:center;font-size:34px;line-height:50px;color:var(--ink)}
.sec-title span{color:var(--heading-blue)}
.sol-card{width:268px;height:228px;border:1px solid #c7c9d4;background:rgba(255,255,255,.35);padding:62px 28px 0}
.sol-card h3{font-family:"Poppins",sans-serif;font-weight:500;font-size:13.5px;color:#222;margin-bottom:16px}
.sol-card p{font-size:12px;line-height:24px}
.sol-icon{width:56px;height:56px;border-radius:50%;border:4px solid #fff;display:flex;align-items:center;justify-content:center}
.arrow{width:44px;height:44px;border-radius:50%;display:flex;align-items:center;justify-content:center;color:var(--white);font-size:16px}

/* work */
.work-title{left:144px;top:3030px;font-size:34px;color:var(--ink)}
.work-title span{color:var(--heading-blue)}
.work-text{left:144px;top:3088px;width:620px;font-size:12px;line-height:24px}
.case-img{height:250px}
.case h3{font-family:"Poppins",sans-serif;font-weight:500;font-size:14px;color:#222;margin:14px 0 8px}
.case p{font-size:12px;line-height:24px}

/* testimonials */
.testi-bg{left:0;top:3660px;width:1200px;height:512px;background:linear-gradient(135deg,#ffffff 0%,#eef0f7 50%,#e6e8f2 100%)}
.t-card{width:308px;height:226px;background:var(--white);border-radius:6px;box-shadow:0 4px 16px rgba(30,40,80,.08);padding:34px 36px 0}
.t-head{display:flex;align-items:center;gap:14px;margin-bottom:16px}
.avatar{width:52px;height:52px;border-radius:50%;background:linear-gradient(160deg,#9aa3b5,#4b556a);flex:none}
.t-name{font-size:13px;font-weight:600;color:#222;line-height:16px}
.t-name small{display:block;font-size:10px;font-weight:400;color:#555}
.rating{margin-left:auto;display:flex;align-items:center;gap:4px;font-size:10px;color:#f5a623}
.rate-dot{width:14px;height:14px;border-radius:50%;background:#c8ccd6}
.t-card p{font-size:11px;line-height:22px;color:#666}

/* faq */
.faq{left:201px;top:4344px;width:798px;list-style:none}
.faq li{height:62px;background:#eef0f3;margin-bottom:15px;display:flex;align-items:center;justify-content:space-between;padding:0 28px;font-size:17px;font-weight:500;color:#222}

/* footer */
.footer{left:0;top:4998px;width:1200px;height:293px;background:var(--navy-deep)}
.copy{left:0;width:1200px;top:5216px;text-align:center;font-size:11px;color:#d8dce6}
</style>
</head>
<body>

<section class="hero abs">
  <div class="hero-photo abs" role="img" aria-label="Flooded residential street with rescuers paddling a boat at dusk"></div>
  <div class="hero-shade abs"></div>

  <a class="brand abs" style="left:144px;top:34px"><span class="brand-mark"></span>Ridgeline</a>

  <div class="call abs" style="left:668px;top:28px">
    <span class="call-icon"><svg width="14" height="14" viewBox="0 0 24 24" fill="#fff"><path d="M6.6 10.8a15 15 0 0 0 6.6 6.6l2.2-2.2a1 1 0 0 1 1-.25 11.4 11.4 0 0 0 3.6.57 1 1 0 0 1 1 1V20a1 1 0 0 1-1 1A17 17 0 0 1 3 4a1 1 0 0 1 1-1h3.5a1 1 0 0 1 1 1c0 1.250.2 2.45.57 3.6a1 1 0 0 1-.25 1z"/></svg></span>
    <span><small>Call us Today</small><strong>(555) 014-2280</strong></span>
  </div>
  <a class="btn abs" style="left:871px;top:27px;width:183px;height:37px">Speak with an expert</a>

  <nav class="nav abs" style="left:465px;top:101px"><span>Home</span><span>About</span><span>Services</span><span>Courses</span><span>Blog</span><span>Contact</span></nav>
  <div class="location abs" style="left:908px;top:101px">
    <svg width="9" height="12" viewBox="0 0 10 14"><path d="M5 0a5 5 0 0 1 5 5c0 3.5-5 9-5 9S0 8.5 0 5a5 5 0 0 1 5-5z" fill="var(--orange)"/><circle cx="5" cy="5" r="2" fill="#2a2440"/></svg>Head Office Location
  </div>

  <h1 class="hero-title abs">MINIMIZE RISK.</h1>
  <h2 class="hero-title2 abs">MITIGATE LOSS</h2>
  <p class="hero-sub abs">COMMAND CHAOS WITH CONFIDENCE</p>

  <div class="play abs"><svg width="22" height="24" viewBox="0 0 22 24"><path d="M2 1l19 11L2 23z" fill="#111"/></svg></div>
  <div class="dots abs"><span></span><span></span><span></span><span style="opacity:.6"></span></div>

  <svg class="abs" style="left:0;top:700px" width="1200" height="90" viewBox="0 0 1200 90">
    <path d="M0 60 Q600 20 1200 0 L1200 90 L0 90 Z" fill="#eef0f6"/>
    <path d="M0 60 L0 80 Q300 50 560 38 Q860 30 1200 10 L1200 0 Q600 20 0 60Z" fill="var(--navy)"/>
  </svg>
</section>

<div class="intro-bg abs"></div>
<p class="intro abs">When incidents happen, your plans have to work in real time—not just on paper. The Ridgeline Consulting team understands the practical realities that unfold with emergencies having come from distinguished roles in the military, police, firefighting and paramedic fields. This experience has evolved their collective knowledge and education to prepare high risk organizations with clear strategies, operationally realistic plans, and training that builds true capability.</p>

<div class="leader-photo abs" role="img" aria-label="Portrait of the company president in a dark blazer"></div>
<h2 class="why-title abs">WHY CHOOSE<br><span>RIDGELINE CONSULTING</span></h2>
<div class="why-text abs">
  <p>Lorem ipsum dolor sit amet, consectetur adipiscing elit, sed do eiusmod tempor incididunt ut labore et dolore magna aliqua. Ut enim ad minim veniam,</p>
  <p>Lorem ipsum dolor sit amet, consectetur adipiscing elit, sed do eiusmod tempor incididunt ut labore et dolore magna aliqua. Ut enim ad minim veniam,</p>
</div>
<ul class="checks abs">
  <li><svg width="14" height="14" viewBox="0 0 14 14"><circle cx="7" cy="7" r="7" fill="#2b7fc4"/><path d="M4 7.2l2 2 4-4" stroke="#fff" stroke-width="1.6" fill="none"/></svg>Lorem ipsum dolor sit amet, consectetur</li>
  <li><svg width="14" height="14" viewBox="0 0 14 14"><circle cx="7" cy="7" r="7" fill="#2b7fc4"/><path d="M4 7.2l2 2 4-4" stroke="#fff" stroke-width="1.6" fill="none"/></svg>Lorem ipsum dolor sit amet, consectetur</li>
  <li><svg width="14" height="14" viewBox="0 0 14 14"><circle cx="7" cy="7" r="7" fill="#2b7fc4"/><path d="M4 7.2l2 2 4-4" stroke="#fff" stroke-width="1.6" fill="none"/></svg>Lorem ipsum dolor sit amet, consectetur</li>
  <li><svg width="14" height="14" viewBox="0 0 14 14"><circle cx="7" cy="7" r="7" fill="#2b7fc4"/><path d="M4 7.2l2 2 4-4" stroke="#fff" stroke-width="1.6" fill="none"/></svg>Lorem ipsum dolor sit amet, consectetur</li>
</ul>
<blockquote class="quote abs">You won't find a more dedicated, passionate and experienced team that is driven to amplify your readiness and create confident capable leaders for any event that comes your way.<strong>Martin Keller, MA, President</strong></blockquote>

<div class="stats abs">
  <div class="stat" style="margin-left:94px"><b>12</b>Years</div>
  <div class="stat-sep" style="margin-left:40px"></div>
  <div class="stat" style="margin-left:40px"><b>150</b>Clients</div>
  <div class="stat-sep" style="margin-left:40px"></div>
  <div class="stat" style="margin-left:48px"><b>5600+</b>ICS Certifications</div>
</div>

<h3 class="trusted abs">TRUSTED BY INDUSTRY LEADERS</h3>
<div class="logos abs">
  <div class="logo-tile">Northvale Energy</div>
  <div class="logo-tile">Prairie State University</div>
  <div class="logo-tile">Brightmere Midstream</div>
  <div class="logo-tile">Coastline Power</div>
  <div class="logo-tile">Fieldgrow</div>
</div>
<a class="btn view-btn abs">View All Industries &amp; Clients</a>

<section class="solutions abs">
  <h2 class="sec-title abs" style="top:100px">OUR EMERGENCY MANAGEMENT SOLUTIONS<br><span>THAT ADDRESS YOUR CURRENT PRIORITIES</span></h2>

  <div class="arrow abs" style="left:87px;top:338px;background:var(--purple-soft)">&laquo;</div>
  <div class="arrow abs" style="left:1069px;top:338px;background:var(--blue-soft)">&raquo;</div>

  <div class="sol-card abs" style="left:162px;top:267px"><h3>Emergency Management</h3><p>Lorem ipsum dolor sit amet, cons ectetur adipiscing elit, sed do eiusmod tempor</p></div>
  <div class="sol-card abs" style="left:466px;top:267px"><h3>Leadership Development</h3><p>Lorem ipsum dolor sit amet, cons ectetur adipiscing elit, sed do eiusmod tempor</p></div>
  <div class="sol-card abs" style="left:769px;top:267px"><h3>Fire &amp; Life Safety</h3><p>Lorem ipsum dolor sit amet, cons ectetur adipiscing elit, sed do eiusmod tempor</p></div>

  <div class="sol-icon abs" style="left:188px;top:236px;background:var(--navy)"><svg width="22" height="22" viewBox="0 0 24 24" fill="none" stroke="#fff" stroke-width="2"><circle cx="12" cy="12" r="9"/><path d="M12 7v5l3 3"/></svg></div>
  <div class="sol-icon abs" style="left:492px;top:236px;background:var(--purple)"><svg width="22" height="22" viewBox="0 0 24 24" fill="none" stroke="#fff" stroke-width="2"><circle cx="12" cy="8" r="4"/><path d="M4 21c1-4 4-6 8-6s7 2 8 6"/></svg></div>
  <div class="sol-icon abs" style="left:795px;top:236px;background:var(--navy)"><svg width="22" height="22" viewBox="0 0 24 24" fill="none" stroke="#fff" stroke-width="2"><path d="M12 2l8 3v6c0 5-3.5 9-8 11-4.5-2-8-6-8-11V5z"/></svg></div>
</section>

<h2 class="work-title abs">OUR <span>WORK</span></h2>
<p class="work-text abs">Lorem ipsum dolor sit amet, consectetur adipiscing elit, sed do eiusmod tempor incididunt ut labore et dolore magna aliqua. Ut enim ad minim veniam,</p>
<div class="arrow abs" style="left:1015px;top:3030px;background:var(--purple-soft)">&laquo;</div>
<div class="arrow abs" style="left:1069px;top:3030px;background:var(--blue-soft)">&raquo;</div>

<article class="case abs" style="left:144px;top:3175px;width:393px">
  <div class="case-img" role="img" aria-label="Firefighter standing beside a grass wildfire" style="background:linear-gradient(180deg,#5a6a7a 0%,#c5542a 55%,#3c3a38 100%)"></div>
  <h3>Case Study 1</h3><p>Lorem ipsum dolor sit amet, consectetur adipiscing elit, sed do eiusmod tempor incididunt</p>
</article>
<article class="case abs" style="left:551px;top:3175px;width:345px">
  <div class="case-img" role="img" aria-label="Rescue crews searching storm debris" style="height:218px;background:linear-gradient(180deg,#8a8f95 0%,#6b5a4c 50%,#4a3e36 100%)"></div>
  <h3>Case Study 2</h3><p style="text-align:justify">Lorem ipsum dolor sit amet, consectetur adipiscing elit, sed do eiusmod</p>
</article>
<article class="case abs" style="left:908px;top:3175px;width:345px">
  <div class="case-img" role="img" aria-label="Black smoke rising from an industrial fire" style="height:218px;background:linear-gradient(180deg,#2a2a2e 0%,#55504c 55%,#c4641e 100%)"></div>
  <h3>Case Study 2</h3><p style="text-align:justify">Lorem ipsum dolor sit amet, consectetur adipiscing elit, sed do eiusmod</p>
</article>

<div class="testi-bg abs"></div>
<h2 class="sec-title abs" style="top:3722px">WHAT OUR <span>CLIENTS ARE SAYING</span></h2>

<div class="t-card abs" style="left:117px;top:3822px">
  <div class="t-head"><span class="avatar" role="img" aria-label="Client portrait"></span><span class="t-name">Daniel Reyes<small>United State</small></span><span class="rating"><span class="rate-dot"></span>★★★★★</span></div>
  <p>Lorem ipsum dolor sit amet, consectetur adipiscing elit, sed do eiusmod tempor incididunt ut labore et dolore magna aliqua. Ut enim ad minim veniamea .</p>
</div>
<div class="t-card abs" style="left:450px;top:3822px">
  <div class="t-head"><span class="avatar" role="img" aria-label="Client portrait"></span><span class="t-name">Priya Lal<small>United State</small></span><span class="rating"><span class="rate-dot"></span>★★★★★</span></div>
  <p>Lorem ipsum dolor sit amet, consectetur adipiscing elit, sed do eiusmod tempor incididunt ut labore et dolore magna aliqua. Ut enim ad minim veniamea .</p>
</div>
<div class="t-card abs" style="left:781px;top:3822px">
  <div class="t-head"><span class="avatar" role="img" aria-label="Client portrait"></span><span class="t-name">Owen Marsh<small>United State</small></span><span class="rating"><span class="rate-dot"></span>★★★★★</span></div>
  <p>Lorem ipsum dolor sit amet, consectetur adipiscing elit, sed do eiusmod tempor incididunt ut labore et dolore magna aliqua. Ut enim ad minim veniamea .</p>
</div>
<div class="arrow abs" style="left:85px;top:3914px;background:var(--purple-soft)">&laquo;</div>
<div class="arrow abs" style="left:1069px;top:3914px;background:var(--blue-soft)">&raquo;</div>

<h2 class="sec-title abs" style="top:4262px">FREQUENTLY <span>ASKED QUESTIONS</span></h2>
<ul class="faq abs">
  <li>How do you assess and mitigate risks?<span>&#8964;</span></li>
  <li>What technologies do you leverage in emergency management?<span>&#8964;</span></li>
  <li>Do you provide onsite crisis support?<span>&#8964;</span></li>
  <li>Do you provide post-incident reports and analysis?<span>&#8964;</span></li>
  <li>What is your fee structure?<span>&#8964;</span></li>
  <li>Do you provide crisis communication training?<span>&#8964;</span></li>
  <li>What are high-risk industries?<span>&#8964;</span></li>
</ul>

<footer class="footer abs">
  <a class="brand abs" style="left:144px;top:60px"><span class="brand-mark"></span>Ridgeline</a>
  <div class="call abs" style="left:668px;top:56px">
    <span class="call-icon"><svg width="14" height="14" viewBox="0 0 24 24" fill="#fff"><path d="M6.6 10.8a15 15 0 0 0 6.6 6.6l2.2-2.2a1 1 0 0 1 1-.25 11.4 11.4 0 0 0 3.6.57 1 1 0 0 1 1 1V20a1 1 0 0 1-1 1A17 17 0 0 1 3 4a1 1 0 0 1 1-1h3.5a1 1 0 0 1 1 1c0 1.25.2 2.45.57 3.6a1 1 0 0 1-.25 1z"/></svg></span>
    <span><small>Call us Today</small><strong>(555) 014-2280</strong></span>
  </div>
  <a class="btn abs" style="left:871px;top:53px;width:183px;height:37px">Online Training Portal</a>
  <nav class="nav abs" style="left:362px;top:128px"><span>Home</span><span>About</span><span>Services</span><span>Courses</span><span>Blog</span><span>Contact</span></nav>
  <div class="location abs" style="left:804px;top:128px">
    <svg width="9" height="12" viewBox="0 0 10 14"><path d="M5 0a5 5 0 0 1 5 5c0 3.5-5 9-5 9S0 8.5 0 5a5 5 0 0 1 5-5z" fill="var(--orange)"/><circle cx="5" cy="5" r="2" fill="#17284a"/></svg>Eastport + Westbrook Offices
  </div>
  <span class="abs" style="left:1036px;top:124px;width:16px;height:16px;background:#fff;border-radius:2px"></span>
</footer>
<p class="copy abs">Copyright@2026 All Rights Reserved</p>

</body>
</html>
```